Business Card for Interior Designer

I have a logo but want to modify it a little for the business card. Somehow I did it on one of the apps in Adobe - but I'm not proficient enough in adobe to modify it. I'd like to take out the wooden background and make it work for a standard size business card (rectangular not square). I'd also like to have options for the design - Patterns like houndstooth, grass cloth, floral, polkadot - stuff like that but in subtle/classic colors. I also like wreaths (boxwood/magnolia/eucalyptus) and would like to incorporate that as well.

```html
<!DOCTYPE html>
<html lang="en">
<head>
<meta charset="UTF-8">
<title>Ivy &amp; Linden Design – Business Card</title>
<link rel="stylesheet" href="https://fonts.googleapis.com/css2?family=Questrial&family=Allura&display=swap">
<style>
  :root {
    --backdrop: #2a2a2c;
    --card-white: #ffffff;
    --card-tan: #e9b46c;
    --card-tan-light: #efc283;
    --card-tan-dark: #e0a95e;
    --gold: #e2a24c;
    --ink: #141210;
  }
  * { margin: 0; padding: 0; box-sizing: border-box; }
  html, body {
    width: 1200px; height: 800px; overflow: hidden;
    background: var(--backdrop);
  }
  .stage {
    width: 1200px; height: 800px;
    display: flex; align-items: center; justify-content: center; gap: 50px;
  }
  .card {
    width: 540px; height: 309px;
    position: relative;
    font-family: "Questrial", "Century Gothic", sans-serif;
    box-shadow: 0 10px 30px rgba(0,0,0,0.45);
  }
  .card--front { background: var(--card-white); display: flex; align-items: center; justify-content: center; }
  .card--back {
    background:
      repeating-linear-gradient(90deg, rgba(255,255,255,0.05) 0 2px, rgba(0,0,0,0.025) 2px 5px),
      linear-gradient(135deg, var(--card-tan-light), var(--card-tan) 55%, var(--card-tan-dark));
    color: var(--ink);
  }
  .brand {
    display: flex; align-items: center; gap: 10px;
    font-size: 20px; letter-spacing: 0.5px; white-space: nowrap;
  }
  .brand__dot {
    width: 14px; height: 14px; border-radius: 50%;
    background: currentColor;
  }
  .card--front .brand { color: var(--gold); }
  .card--back .brand {
    position: absolute; left: 40px; top: 50%; transform: translateY(-50%);
    color: var(--ink);
  }
  .contact {
    position: absolute; left: 290px; top: 42px;
    font-size: 13.5px; line-height: 1.45;
  }
  .contact__name {
    font-family: "Allura", cursive;
    font-size: 42px; line-height: 1; margin-bottom: 2px;
  }
  .contact__role { font-size: 15px; margin-bottom: 16px; }
  .contact__address { margin-bottom: 14px; }
  .contact__web { margin-top: 12px; }
</style>
</head>
<body>
  <main class="stage">
    <section class="card card--front" aria-label="Card front">
      <div class="brand">
        <span class="brand__dot"></span>
        <span class="brand__name">Ivy &amp; Linden Design</span>
      </div>
    </section>

    <section class="card card--back" aria-label="Card back">
      <div class="brand">
        <span class="brand__dot"></span>
        <span class="brand__name">Ivy &amp; Linden Design</span>
      </div>
      <div class="contact">
        <p class="contact__name">Nora Bell</p>
        <p class="contact__role">Designer</p>
        <p class="contact__address">PO Box 48, Orchard Street<br>3rd Lane, Arizona 85012</p>
        <p class="contact__phone">P: 555.210.4873</p>
        <p class="contact__email">E: hello@ivylinden.com</p>
        <p class="contact__web">www.ivylinden.com</p>
      </div>
    </section>
  </main>
</body>
</html>
```